All Natural Mosquito Repellent

My company, BrightFern Company has created an all natural mosquito repellent. I already have other all natural products that I have developed and created labels for. I will include a copy of that label so you have something to work from. I will need two labels. One for the front of the bottle and one for the back. The back label will need space for a UPC. The labels need to be 63mm (H) x 39mm (W)

Target Market(s)

Consumers, Organic, People who like natural products

Font styles to use
Other font styles liked:
• A combination of both Serif and Sans Serif

Requirements
Must have
• Use the words Organic, All Natural, Travel size, made in the USA label
Nice to have
• tag line: Don't beat them off. Spray them away.

```html
<!DOCTYPE html>
<html lang="en">
<head>
<meta charset="utf-8">
<title>BrightFern Company — Mosquito Repellent Labels</title>
<link rel="stylesheet" href="https://fonts.googleapis.com/css2?family=Bebas+Neue&family=Dancing+Script:wght@700&family=Roboto+Slab:wght@600;700&display=swap">
<style>
  :root {
    --backdrop: #403a35;
    --label: #ffffff;
    --ink: #3f3a35;
    --green: #33d64f;
    --orange: #ff5208;
    --insect: #3b3d40;
  }
  html, body {
    margin: 0;
    width: 1200px;
    height: 1200px;
    overflow: hidden;
    background: var(--backdrop);
  }
  .canvas { position: relative; width: 1200px; height: 1200px; }
  .label {
    position: absolute;
    top: 278px;
    width: 370px;
    height: 596px;
    background: var(--label);
    box-shadow: 0 10px 24px rgba(0,0,0,.35);
    overflow: hidden;
  }
  .label--front { left: 218px; }
  .label--back { left: 612px; }

  .brand {
    position: absolute;
    left: 0; right: 0;
    display: flex; align-items: center; justify-content: center; gap: 8px;
    font-family: "Roboto Slab", serif;
    font-weight: 700;
    color: var(--ink);
    letter-spacing: .3px;
  }
  .brand__dot { width: 12px; height: 12px; border-radius: 50%; background: var(--green); }
  .label--front .brand { top: 100px; font-size: 19px; }
  .label--back .brand { top: 114px; font-size: 17px; }

  .organic {
    position: absolute; left: 0; right: 0;
    text-align: center;
    font-family: "Dancing Script", cursive;
    font-weight: 700;
    color: var(--green);
    line-height: 1;
  }
  .label--front .organic { top: 262px; font-size: 74px; transform: translateY(-60px); }
  .label--back .organic { top: 388px; font-size: 44px; }

  .leaves { position: absolute; }
  .insect { position: absolute; }

  .tagline {
    position: absolute; left: 0; right: 0;
    text-align: center;
    font-family: "Bebas Neue", sans-serif;
    color: #fff;
    font-size: 25px;
    line-height: 26px;
  }
  .tagline--top { top: 301px; height: 26px; background: var(--orange); }
  .tagline--bottom { top: 328px; height: 26px; background: var(--ink); padding-top: 0; }

  .badge {
    position: absolute; top: 399px;
    width: 74px; height: 74px;
    border: 2.5px solid var(--green);
    border-radius: 50%;
    box-sizing: border-box;
    display: flex; align-items: center; justify-content: center;
  }
  .badge__core {
    width: 60px; height: 60px; border-radius: 50%;
    display: flex; align-items: center; justify-content: center;
    text-align: center;
    font-family: "Roboto Slab", serif; font-weight: 700;
    font-size: 13.5px; line-height: 12px; color: #fff;
  }
  .badge--natural { left: 107px; }
  .badge--natural .badge__core { background: var(--green); }
  .badge--travel { left: 193px; }
  .badge--travel .badge__core { background: var(--ink); }

  .flag {
    position: absolute; left: 158px; top: 512px;
    width: 55px; height: 29px;
  }
  .made-in {
    position: absolute; left: 0; right: 0; top: 552px;
    text-align: center;
    font-family: "Roboto Slab", serif; font-weight: 700;
    font-size: 16px; color: var(--orange);
  }

  .info-box {
    position: absolute; left: 42px; top: 184px;
    width: 286px; height: 179px;
    background: var(--ink);
    color: #fff;
    font-family: "Roboto Slab", serif; font-weight: 700;
    font-size: 12px; line-height: 14px;
    text-align: center;
    box-sizing: border-box;
    padding: 31px 38px 0;
  }
  .info-box p { margin: 0 0 14px; }
</style>
</head>
<body>
<div class="canvas">

  <section class="label label--front">
    <div class="brand"><span class="brand__dot"></span>BrightFern Company</div>

    <svg class="insect" style="left:302px;top:156px" width="48" height="40" role="img" aria-label="mosquito illustration"><ellipse cx="24" cy="20" rx="18" ry="7" fill="var(--insect)" opacity=".85"/></svg>
    <svg class="insect" style="left:142px;top:192px" width="40" height="34" role="img" aria-label="mosquito illustration"><ellipse cx="20" cy="17" rx="15" ry="6" fill="var(--insect)" opacity=".85"/></svg>

    <div class="organic">Organic</div>
    <svg class="leaves" style="left:250px;top:190px" width="54" height="48" role="img" aria-label="pair of green leaves"><ellipse cx="27" cy="24" rx="24" ry="20" fill="var(--green)"/></svg>

    <div class="tagline tagline--top">DON'T BEAT THEM OFF.</div>
    <div class="tagline tagline--bottom">SPRAY THEM AWAY.</div>

    <svg class="insect" style="left:304px;top:380px" width="44" height="38" role="img" aria-label="mosquito illustration"><ellipse cx="22" cy="19" rx="17" ry="7" fill="var(--insect)" opacity=".85"/></svg>
    <svg class="insect" style="left:32px;top:436px" width="42" height="32" role="img" aria-label="mosquito illustration"><ellipse cx="21" cy="16" rx="16" ry="6" fill="var(--insect)" opacity=".85"/></svg>

    <div class="badge badge--natural"><div class="badge__core">All<br>Natural</div></div>
    <div class="badge badge--travel"><div class="badge__core">Travel<br>size</div></div>

    <svg class="flag" viewBox="0 0 55 29" role="img" aria-label="United States flag">
      <rect width="55" height="29" fill="var(--ink)"/>
      <rect y="3" width="55" height="2" fill="#fff"/><rect y="9" width="55" height="2" fill="#fff"/>
      <rect y="15" width="55" height="2" fill="#fff"/><rect y="21" width="55" height="2" fill="#fff"/>
      <rect y="27" width="55" height="2" fill="#fff"/>
    </svg>

    <svg class="insect" style="left:32px;top:536px" width="38" height="32" role="img" aria-label="mosquito illustration"><ellipse cx="19" cy="16" rx="14" ry="6" fill="var(--insect)" opacity=".85"/></svg>
    <svg class="insect" style="left:300px;top:528px" width="40" height="32" role="img" aria-label="mosquito illustration"><ellipse cx="20" cy="16" rx="15" ry="6" fill="var(--insect)" opacity=".85"/></svg>

    <div class="made-in">made in the USA label</div>
  </section>

  <section class="label label--back">
    <div class="brand"><span class="brand__dot"></span>BrightFern Company</div>

    <div class="info-box">
      <p>Lorem ipsum dolor sit amet, consectetuer adipiscing elit, sed diam nonummy nibh euismod tincidunt</p>
      <p>ut laoreet dolore magna aliquam erat volutpat. Ut wisi enim ad minim veniam, quis nostrud exerci tation ullamcorper</p>
    </div>

    <div class="organic">Organic</div>
    <svg class="leaves" style="left:224px;top:380px" width="34" height="30" role="img" aria-label="pair of green leaves"><ellipse cx="17" cy="15" rx="15" ry="12" fill="var(--green)"/></svg>
  </section>

</div>
</body>
</html>
```